Harborline Security and Surveillance Business Card

Business Card Design - Company Name:Freedom Security and SurveillanceWe are a Security Systems Integrator Specializing in Security Systems/ Video Surveillance and Access Control. Our areas of expertise are:Security SystemsVideo SurveillanceAccess ControlFire Alarm SystemsNetwork CablingCellular BoostersMy input is the Front of the Card is: logo, name of Business, My Name, Phone Number, and email.Rear of Card is the 6 areas of expertise, I just dont want the front to be very busy.
Name: Tom Jenner
Title: President
Email: tom@harborlinesecuritysys.example
website: harborlinesecuritysys.example

```html
<!DOCTYPE html>
<html lang="en">
<head>
<meta charset="utf-8">
<title>Harborline Security and Surveillance – Business Card</title>
<link href="https://fonts.googleapis.com/css2?family=Lato:wght@400;700&family=Saira:wght@600&display=swap" rel="stylesheet">
<style>
  :root {
    --backdrop: #404040;
    --card-white: #ffffff;
    --brand-blue: #075cbb;
    --ink: #454545;
    --shadow: rgba(0, 0, 0, 0.55);
  }
  * { margin: 0; padding: 0; box-sizing: border-box; }
  html, body {
    width: 1200px;
    height: 900px;
    overflow: hidden;
    background: var(--backdrop);
  }
  .canvas {
    position: relative;
    width: 1200px;
    height: 900px;
  }
  .card {
    position: absolute;
    top: 200px;
    width: 310px;
    height: 502px;
    box-shadow: 4px 5px 6px var(--shadow);
  }
  .card-front {
    left: 253px;
    background: var(--card-white);
    border-radius: 56px 0 56px 0;
  }
  .card-back {
    left: 627px;
    width: 309px;
    background: var(--brand-blue);
    border-radius: 0 56px 0 56px;
  }

  /* Front */
  .brand {
    position: absolute;
    top: 118px;
    left: 0;
    width: 100%;
    text-align: center;
    color: var(--brand-blue);
    font-family: "Saira", sans-serif;
    font-weight: 600;
  }
  .brand-dot {
    display: block;
    width: 44px;
    height: 44px;
    margin: 0 auto 12px;
    border-radius: 50%;
    background: var(--brand-blue);
  }
  .brand-name {
    font-size: 20px;
    letter-spacing: 0.5px;
    line-height: 1.1;
  }
  .brand-tagline {
    font-size: 10px;
    letter-spacing: 1.6px;
    margin-top: 3px;
  }
  .holder-name {
    position: absolute;
    left: 33px;
    top: 358px;
    color: var(--brand-blue);
    font-family: "Saira", sans-serif;
    font-weight: 600;
    font-size: 21px;
    letter-spacing: 0.3px;
  }
  .contact {
    position: absolute;
    left: 33px;
    top: 418px;
    list-style: none;
    font-family: "Lato", sans-serif;
    font-size: 14.5px;
    color: var(--ink);
    line-height: 21px;
  }
  .contact li {
    display: flex;
    align-items: center;
    gap: 5px;
  }
  .contact svg { fill: var(--brand-blue); flex: none; }

  /* Back */
  .back-brand {
    position: absolute;
    top: 178px;
    left: 0;
    width: 100%;
    text-align: center;
    color: var(--card-white);
    font-family: "Saira", sans-serif;
    font-weight: 600;
  }
  .back-brand .brand-dot {
    width: 80px;
    height: 80px;
    margin-bottom: 14px;
    background: var(--card-white);
  }
  .back-brand .brand-name { font-size: 22px; letter-spacing: 1px; }
  .services {
    position: absolute;
    top: 400px;
    left: 0;
    width: 100%;
    text-align: center;
    color: var(--card-white);
    font-family: "Lato", sans-serif;
    font-size: 14.5px;
    line-height: 18px;
  }
  .services .sep {
    display: inline-block;
    width: 9px;
    height: 9px;
    margin: 0 3px 1px;
    border-radius: 50%;
    background: var(--card-white);
  }
</style>
</head>
<body>
<main class="canvas">
  <section class="card card-front" aria-label="Card front">
    <div class="brand">
      <span class="brand-dot"></span>
      <div class="brand-name">HARBORLINE SECURITY</div>
      <div class="brand-tagline">AND SURVEILLANCE</div>
    </div>
    <h1 class="holder-name">TOM JENNER</h1>
    <ul class="contact">
      <li>
        <svg width="16" height="13" viewBox="0 0 16 13" aria-hidden="true">
          <path d="M1 4c0-2 3-3.2 7-3.2S15 2 15 4v1.4h-3.2V3.6C10.6 3.2 5.4 3.2 4.2 3.6v1.8H1z"/>
          <path d="M4.5 5.2h7L14 12.5H2z"/>
        </svg>
        044-555 010 234
      </li>
      <li>
        <svg width="14" height="11" viewBox="0 0 14 11" aria-hidden="true">
          <rect x="0" y="0" width="14" height="11" rx="1"/>
          <path d="M1 1.2l6 5 6-5" fill="none" stroke="#fff" stroke-width="1.2"/>
        </svg>
        tom@harborlinesecuritysys.example
      </li>
    </ul>
  </section>

  <section class="card card-back" aria-label="Card back">
    <div class="back-brand">
      <span class="brand-dot"></span>
      <div class="brand-name">HARBORLINE</div>
    </div>
    <p class="services">
      Security Systems<span class="sep"></span>Video Surveillance<br>
      Access Control<span class="sep"></span>Fire Alarm Systems<br>
      Network Cabling<span class="sep"></span>Cellular Boosters
    </p>
  </section>
</main>
</body>
</html>
```